Welding company needs a business card

We are looking for a logo and business card.

Contact Information for Business Card

418 Cobblestone Lane
York, PA 17402
410-555-0173
Rmfabworksco@quorvamail.com

```html
<!DOCTYPE html>
<html lang="en">
<head>
<meta charset="utf-8">
<title>RM Fabworks Co — Business Card</title>
<link href="https://fonts.googleapis.com/css2?family=Lato:wght@400;700&display=swap" rel="stylesheet">
<style>
  :root {
    --bg: #8c8c8c;
    --card-light: #ffffff;
    --card-dark: #2b2b2b;
    --card-dark-glow: #3a3a3a;
    --ink: #2a2a2a;
    --ink-soft: #3c3c3c;
    --rule: #9a9a9a;
    --reverse: #ffffff;
  }
  * { box-sizing: border-box; margin: 0; padding: 0; }
  html, body { width: 1200px; height: 1200px; overflow: hidden; }
  body {
    background: var(--bg);
    position: relative;
    font-family: "Lato", Arial, sans-serif;
  }
  .card {
    position: absolute;
    top: 310px;
    width: 364px;
    height: 594px;
  }
  .card--front { left: 234px; background: var(--card-light); }
  .card--back {
    left: 627px;
    width: 368px;
    background: var(--card-dark);
    overflow: hidden;
  }
  .brand {
    position: absolute;
    left: 0; right: 0;
    display: flex;
    align-items: center;
    justify-content: center;
    gap: 12px;
    font-weight: 700;
    text-transform: uppercase;
    letter-spacing: 1px;
    white-space: nowrap;
  }
  .brand__mark { display: block; flex: none; }
  .card--front .brand { top: 200px; font-size: 27px; color: var(--ink); }
  .card--front .brand__mark { width: 30px; height: 30px; background: var(--ink); }
  .card--back .brand { top: 276px; font-size: 30px; color: var(--reverse); }
  .card--back .brand__mark { width: 34px; height: 34px; background: var(--reverse); }

  .contact {
    position: absolute;
    top: 375px;
    left: 0; right: 0;
    text-align: center;
    color: var(--ink-soft);
  }
  .contact__name {
    font-weight: 700;
    font-size: 21px;
    letter-spacing: 0.5px;
    color: var(--ink);
    line-height: 26px;
  }
  .contact__title { font-size: 16px; line-height: 20px; }
  .contact__rule {
    width: 154px;
    height: 1px;
    background: var(--rule);
    margin: 10px auto 10px;
  }
  .contact__line { font-size: 16px; line-height: 21px; }

  .backdrop {
    position: absolute;
    inset: 0;
    background: radial-gradient(ellipse at 50% 50%, var(--card-dark-glow) 0%, var(--card-dark) 70%);
  }
</style>
</head>
<body>
  <section class="card card--front">
    <div class="brand"><span class="brand__mark"></span>RM Fabworks Co</div>
    <div class="contact">
      <p class="contact__name">DANIEL CARTER</p>
      <p class="contact__title">Managing Director</p>
      <div class="contact__rule"></div>
      <p class="contact__line">418 Cobblestone Lane</p>
      <p class="contact__line">York, PA 17402</p>
      <div class="contact__rule"></div>
      <p class="contact__line">410-555-0173</p>
      <p class="contact__line">Rmfabworksco@quorvamail.com</p>
    </div>
  </section>

  <section class="card card--back">
    <div class="backdrop" role="img" aria-label="Faint geometric shard pattern in dark grey"></div>
    <div class="brand"><span class="brand__mark"></span>RM Fabworks</div>
  </section>
</body>
</html>
```